Modern business card design

Looking for a modern business card layout with on the one side the logo (blue or white version) and on the other side the information such as name, email, phone numbers, website and QR code.
Enclosed the logo, the info and the QR code to be used. QR code should also give you all the info that could / should be on the card. Also enclosed a few examples of business cards I do like that should give you an idea what I am looking for. The "back of business card ideas" I like for the lay out, the modern business card idea is more because I do like the fact that the colour from the front is used again on the back so it is not just white.
Color codes: HS #D19B2A and HS #D19B2A
Fonts of the logo are: Heading Pro Treble Bold and SangBlue Sans/
See enclosed

```html
<!DOCTYPE html>
<html lang="en">
<head>
<meta charset="utf-8">
<title>ORBIT Air Cargo Experts – Business Card</title>
<link rel="stylesheet" href="https://fonts.googleapis.com/css2?family=Marcellus&family=Montserrat:wght@500;600&family=Roboto:wght@400;700&display=swap">
<style>
  :root{
    --backdrop:#2a2a2b;
    --card:#312c7c;
    --card-deep:#2b2670;
    --gold:#d19b2a;
    --white:#f2f2f6;
    --steel:#5a5a64;
    --steel-dark:#2e2e38;
  }
  *{box-sizing:border-box;margin:0;padding:0}
  html,body{width:1200px;height:1138px;overflow:hidden;background:var(--backdrop)}
  .card{
    position:absolute;width:618px;height:375px;border-radius:16px;
    background:linear-gradient(180deg,var(--card) 0%,var(--card-deep) 100%);
    overflow:hidden;
  }
  .card--front{left:274px;top:186px}
  .card--back{left:277px;top:608px}

  .artwork{
    position:absolute;left:10px;top:95px;width:560px;height:190px;
    transform:rotate(-30deg);transform-origin:center;
    background:radial-gradient(closest-side,var(--steel) 0%,rgba(70,70,82,.85) 40%,rgba(46,46,56,.55) 70%,rgba(49,44,124,0) 100%);
  }
  .wordmark{
    position:absolute;left:346px;top:240px;
    font-family:"Marcellus",serif;font-size:66px;line-height:1;letter-spacing:4px;color:var(--white);
  }
  .tagline{
    font-family:"Montserrat",sans-serif;font-weight:600;color:var(--gold);text-transform:uppercase;
  }
  .card--front .tagline{position:absolute;left:342px;top:297px;font-size:13px;letter-spacing:4.6px}

  .logo-block{position:absolute;left:53px;top:150px;width:250px}
  .logo-block .wordmark{position:static;font-size:58px;letter-spacing:6px;text-align:right}
  .logo-block .tagline{color:var(--white);font-size:11px;letter-spacing:3.6px;text-align:right;margin-top:0}
  .logo-block .byline{
    font-family:"Montserrat",sans-serif;font-weight:500;color:var(--gold);
    font-size:8px;letter-spacing:6.4px;text-align:right;margin-top:3px;text-transform:uppercase;
  }
  .logo-rule{position:absolute;left:53px;top:223px;width:63px;height:1px;background:var(--white)}
  .divider{position:absolute;left:321px;top:82px;width:1px;height:212px;background:var(--gold)}

  .contact{position:absolute;left:345px;top:112px;font-family:"Roboto",sans-serif;color:var(--white)}
  .contact__name{font-weight:700;font-size:29px;color:var(--gold);line-height:1.05;letter-spacing:-.3px}
  .contact__role{font-size:17px;margin-top:2px}
  .contact__list{list-style:none;margin-top:20px}
  .contact__list li{display:flex;align-items:center;font-size:17px;height:25px}
  .contact__list svg{width:14px;height:14px;margin-right:16px;fill:var(--gold)}
</style>
</head>
<body>
  <section class="card card--front">
    <div class="artwork" role="img" aria-label="Embossed illustration of a cargo jet climbing with vapour trails"></div>
    <div class="wordmark">ORBIT</div>
    <div class="tagline">Air Cargo Experts</div>
  </section>

  <section class="card card--back">
    <div class="logo-block">
      <div class="wordmark">ORBIT</div>
      <div class="tagline">Air Cargo Experts</div>
      <div class="byline">by Marten Dukes</div>
    </div>
    <div class="logo-rule"></div>
    <div class="divider"></div>
    <div class="contact">
      <div class="contact__name">Marten Dukes</div>
      <div class="contact__role">Managing Director</div>
      <ul class="contact__list">
        <li><svg viewBox="0 0 16 16" aria-hidden="true"><path d="M3 2h3l1 4-2 1a9 9 0 0 0 4 4l1-2 4 1v3c0 1-1 2-2 2A12 12 0 0 1 1 4c0-1 1-2 2-2z"/></svg>000-111-1111</li>
        <li><svg viewBox="0 0 16 16" aria-hidden="true"><path d="M1 3h14v10H1z M2 4l6 5 6-5" fill="var(--gold)" stroke="var(--card)" stroke-width="1"/></svg>john@yourwebsite.com</li>
        <li><svg viewBox="0 0 16 16" aria-hidden="true"><circle cx="8" cy="8" r="7"/><path d="M1 8h14M8 1c-3 4-3 10 0 14M8 1c3 4 3 10 0 14" fill="none" stroke="var(--card)" stroke-width="1"/></svg>www.yourwebsite.com</li>
      </ul>
    </div>
  </section>
</body>
</html>
```